Webdesign für Naturheilpraktiker gesucht
Zielgruppe
Ich arbeite im Gesundheitswesen als Naturheilpraktiker Traditionell Tibetische Medizin.
Verfüge aber über verschiedene Anwendungstechniken.
Die Zielgruppe sind alle Menschen die mehr als nur klassische Medizin wollen, die mit der klassischen Schulmedizin nicht mehr weiter kommen und einen alternativen Weg suchen. Menschen die neben der Schulmedizin noch einen anderen Weg suchen.
Menschen im Wellness und Fitnessbereich.
Ernährungsbewusste Menschen.
Sportler allgemein da ich über eine neue Technik verfüge (KERVO) die erst auf den Markt kommt und mit der verschiedene Beschwerden gelindert werden können.
Grob gesagt alles was mit Medizin, Komplementärmedizin, Gesundheit, Wellness, Sport usw zu tun hat.
Kompetenzen der Traditionell Tibetische Medizin:
- Massage als Gesundheitssystem oder als Wellness
- Ernährungsberatung
- tibetisches Yoga
- Lebensberatung
- Familienstellen
Aufgabenstellung
Der Firmennamen und das Logo bestehen.
In der Tradition der tibetischen Medizin ist vor allem Blau (Medizin Buddha) die Farben sind aber frei wählbar.
Es soll Vertrautheit, Geborgenheit und Wärme ausstrahlen.
Nicht zu feminin erscheinen.
Einfach ein paar Ideen
http://massagepraxis-wolfrin.example
http://www.himalheilkunde.example

```html
<!DOCTYPE html>
<html lang="de">
<head>
<meta charset="utf-8">
<title>Lunaya – Homöopathie</title>
<link rel="stylesheet" href="https://fonts.googleapis.com/css2?family=Comfortaa:wght@700&family=Open+Sans:wght@300;400;600;700&family=Roboto:wght@300;400&display=swap">
<style>
:root{
  --blue:#1e94d6;
  --green:#79c24d;
  --green-text:#6cb846;
  --ink:#444;
  --muted:#555;
  --white:#fff;
  --rule:#ddd;
}
*{margin:0;padding:0;box-sizing:border-box}
html,body{width:1123px;height:1200px;overflow:hidden;background:var(--white)}
body{position:relative;font-family:"Open Sans",sans-serif;color:var(--ink)}
.abs{position:absolute}
.top-line{left:0;top:0;width:1123px;height:2px;background:var(--green)}
.brand{left:300px;top:30px;display:flex;align-items:center;gap:8px;font-family:"Open Sans",sans-serif;font-weight:600;font-size:16px;color:#2a4e8f;letter-spacing:2px}
.brand-dot{width:22px;height:22px;border-radius:50%;background:var(--blue)}
.nav{left:451px;top:24px;display:flex;align-items:center;font-family:"Roboto",sans-serif;font-size:10.5px;color:#444}
.nav a{text-decoration:none;color:inherit;padding:0 10.5px;line-height:24px}
.nav a.active{background:var(--blue);color:var(--white);padding:0 9px}
.hero{left:0;top:105px;width:1123px;height:250px;background:var(--blue)}
.hero-title{left:252px;top:138px;font-family:"Comfortaa",sans-serif;font-weight:700;font-size:26px;color:var(--white)}
.hero-lead{left:252px;top:183px;width:620px;font-family:"Roboto",sans-serif;font-weight:300;font-size:11.6px;line-height:18px;color:var(--white)}
.tiles{left:252px;top:256px;width:619px;height:311px;display:grid;grid-template-columns:repeat(4,1fr);grid-template-rows:1fr 1fr}
.tile{padding:32px 14px 0}
.tile-light{background:var(--white);color:#555}
.tile-green{background:var(--green);color:var(--white)}
.tile h2{font-weight:300;font-size:19px;line-height:19px;margin-bottom:12px}
.tile p{font-weight:300;font-size:9.3px;line-height:14px;margin-bottom:8px}
.tile-light .more{color:var(--green-text)}
.tile .more{font-size:9.5px}
.photo{width:100%;height:100%}
.intro-title{left:266px;top:598px;font-weight:300;font-size:18px;color:#555}
.intro-text{left:266px;top:630px;width:600px;font-weight:300;font-size:8.6px;line-height:14px;color:#555}
.post-title{left:266px;width:410px;font-weight:400;font-size:19px;line-height:19px;color:var(--green-text)}
.thumb{left:266px;width:117px;height:78px;border:1px solid #e2e2e2;padding:1px}
.thumb div{width:100%;height:100%}
.post-text{left:397px;width:272px;font-weight:300;font-size:8.8px;line-height:14px;color:#555}
.btn{display:flex;align-items:center;justify-content:center;border:1px solid var(--green-text);border-radius:2px;color:var(--green-text);font-family:"Roboto",sans-serif;font-weight:400;font-size:9.5px;font-weight:700}
.btn-small{left:397px;width:82px;height:23px}
.rule{left:266px;width:402px;height:1px;background:var(--rule)}
.doctor{left:692px;top:686px;width:167px;height:143px;border:1px solid #e2e2e2;padding:1px}
.doctor div{width:100%;height:100%}
.doctor-name{left:692px;top:840px;font-family:"Roboto",sans-serif;font-weight:300;font-size:12px;color:#555}
.doctor-note{left:692px;top:875px;font-weight:300;font-size:9.3px;color:#555}
.footer{left:0;top:1161px;width:1123px;height:39px;background:var(--blue);color:var(--white)}
.footer-links{left:252px;top:12px;font-size:8.8px}
.footer-credit{left:841px;top:11px;font-size:10px;font-weight:600}
</style>
</head>
<body>
<div class="abs top-line"></div>

<div class="abs brand"><span class="brand-dot"></span>LUNAYA</div>

<nav class="abs nav">
  <a class="active" href="#">Home</a>
  <a href="#">Geschichte</a>
  <a href="#">Homöopathie</a>
  <a href="#">Information</a>
  <a href="#">Kontakt</a>
</nav>

<section class="abs hero"></section>
<h1 class="abs hero-title">Willkommen</h1>
<p class="abs hero-lead">Immer mehr Menschen vertrauen der Heilwirkung homöopathischer Verfahren. Wir informieren Sie auf unserer Website über die wichtigsten Fragen zu dieser seit Jahrhunderten erprobten alternativen Behandlungsmethode.</p>

<div class="abs tiles">
  <div class="photo" role="img" aria-label="Kind liegt im Bett und hält Globuli in der Hand" style="background:linear-gradient(135deg,#efe9e4,#d8c3b0 50%,#f3f3f3)"></div>
  <div class="tile tile-light">
    <h2>Gesund im Kindesalter</h2>
    <p>Lernen Sie mehr zur Gesundheit Ihrer Kinder</p>
    <span class="more">mehr lesen</span>
  </div>
  <div class="photo" role="img" aria-label="Tasse Kamillentee mit Gänseblümchen" style="background:radial-gradient(circle at 50% 55%,#e9b940 0,#f0d48a 28%,#f4f4f4 60%)"></div>
  <div class="tile tile-light">
    <h2>Kräuter Medizin</h2>
    <p>Hier finden Sie Informationen aus der Welt der Kräuter</p>
    <span class="more">mehr lesen</span>
  </div>
  <div class="tile tile-green">
    <h2>Ingwer Tee</h2>
    <p>Rezepte und Wissenswertes zu Ingwer Tee</p>
    <span class="more">mehr lesen</span>
  </div>
  <div class="photo" role="img" aria-label="Ingwerwurzel mit Glas Ingwertee auf Holztisch" style="background:linear-gradient(160deg,#8a7a68,#c9b48f 50%,#6e5d4a)"></div>
  <div class="tile tile-green">
    <h2>Vorteile von Tee</h2>
    <p>Warum Tee so gut ist für Ihre Gesundheit</p>
    <span class="more">mehr lesen</span>
  </div>
  <div class="photo" role="img" aria-label="Tasse Tee mit frischen Minzblättern und Zitrone" style="background:radial-gradient(circle at 55% 60%,#f1f0e6 0,#e9d37a 22%,#6f8f3a 50%,#6b3e22 85%)"></div>
</div>

<h2 class="abs intro-title">Was ist Homöopathie-Heilkunde?</h2>
<p class="abs intro-text">Die Homöopathie-Therapie ist ein Naturheilverfahren, das bei richtiger Anwendung frei von Nebenwirkungen ist. Auf einem sanften, aber effektiven Weg zielt die Homöopathie auf eine umfassende Behandlung gesundheitlicher Probleme.</p>

<h3 class="abs post-title" style="top:686px">Homöopathie-Heilverfahren: Ideal für Kinder</h3>
<div class="abs thumb" style="top:707px"><div role="img" aria-label="Kind im Bett mit Globuli" style="background:linear-gradient(135deg,#efe9e4,#d8c3b0 50%,#f3f3f3)"></div></div>
<p class="abs post-text" style="top:706px">Homöopathische Mittel eignen sich ganz besonders für die Behandlung von Kindern. Da sie bei ordnungsgemäßer Anwendung keine Nebenwirkungen verursachen, wirken homöopathische Mittel deutlich sanfter als Arzneien der Schulmedizin.</p>
<div class="abs btn btn-small" style="top:784px">mehr</div>
<div class="abs rule" style="top:815px"></div>

<h3 class="abs post-title" style="top:829px">Wann Homöopathie-Verfahren nicht zur Anwendung kommen</h3>
<div class="abs thumb" style="top:867px"><div role="img" aria-label="Homöopathische Fläschchen und Globuli mit Blüten" style="background:linear-gradient(135deg,#6d6457,#b6aa98 50%,#5d5448)"></div></div>
<p class="abs post-text" style="top:867px">Eine homöopathische Behandlung kommt allerdings bei einigen Erkrankungen nicht oder nur ergänzend in Betracht.</p>
<div class="abs btn btn-small" style="top:902px">mehr</div>
<div class="abs rule" style="top:959px"></div>

<h3 class="abs post-title" style="top:972px">Was Ihnen Ihr Arzt über die Homöopathie-Therapie meistens nicht erzählt</h3>
<div class="abs thumb" style="top:1010px"><div role="img" aria-label="Arzt hält die Hand einer Patientin" style="background:linear-gradient(135deg,#f2f2f2,#e4cdbe 55%,#f6f6f6)"></div></div>
<p class="abs post-text" style="top:1010px">Trotz überzeugender Website Erfahrungsberichte von Patienten, die sich homöopathisch behandeln ließen, raten Schulmediziner meist von einer alternativen Behandlung mit homöopathischen Mitteln ab.</p>
<div class="abs btn btn-small" style="top:1074px">mehr</div>

<div class="abs btn" style="left:266px;top:1106px;width:402px;height:28px">Mehr Informationen</div>

<div class="abs doctor"><div role="img" aria-label="Porträt eines Arztes in blauer Kleidung mit Stethoskop" style="background:linear-gradient(180deg,#4f86b3,#3f77a8 60%,#5fa0d0)"></div></div>
<p class="abs doctor-name">Dr. Jonas Berger</p>
<p class="abs doctor-note">Kontaktieren Sie uns für einen Termin</p>
<div class="abs btn" style="left:692px;top:895px;width:165px;height:28px">Kontakt</div>

<footer class="abs footer">
  <span class="abs footer-links">© 2017 Homeopathy | Impressum | Datenschutz | Haftungsausschluss</span>
  <span class="abs footer-credit">sitebau</span>
</footer>
</body>
</html>
```